Business Card and Letterhead Design for Public Accounting Firm

Business card and letterhead design for a CPA Firm located in Orange County, CA. We're looking for a modern and professional design utilizing our existing logo. We'd like a clean "less is more" look, but also something that catches the eye. We provide a high level of service to our clients. Open to single or double sided business cards.

Additional info: color numbers on logo
Blue :
R 0
G 83
B 125

#00537D

Silver :

R 154
G 154
B 154

#9A9A9A

Target Market(s)

Businesses and individuals

Industry/Entity Type

Accounting

Contact Information for Business Card

Moss Whitfield & Danby LLP - 4827 Larkspur Vale Road, Irvine, CA 92614 - (949)731-2864 - mwdaccts.example

Font styles to use
Serif
Sans Serif
Other font styles liked:
• See font file uploaded

Colors
0054AA
0677BA
7BADD7
CADEEF
E8F1F8

Requirements
Nice to have
• Possibly use the font file provided which matches our logo, but adjust to be not in all caps

```html
<!DOCTYPE html>
<html lang="en">
<head>
<meta charset="utf-8">
<title>Moss Whitfield &amp; Danby LLP — Stationery</title>
<link href="https://fonts.googleapis.com/css2?family=Ubuntu:wght@400;500;700&display=swap" rel="stylesheet">
<style>
  :root {
    --brand-blue: #00537D;
    --brand-silver: #9A9A9A;
    --ink-blue: #0a4a78;
    --navy-band: #34475c;
    --pattern-light: #eef0f2;
    --flap-blue: #d3dfe6;
    --paper: #ffffff;
    --backdrop: #e6e6e6;
  }
  * { box-sizing: border-box; margin: 0; padding: 0; }
  html, body { width: 1200px; height: 1200px; overflow: hidden; }
  body {
    background: var(--backdrop);
    font-family: "Ubuntu", Arial, sans-serif;
    position: relative;
  }

  /* Letterhead */
  .letterhead {
    position: absolute; left: 40px; top: 200px;
    width: 565px; height: 800px;
    background: var(--paper);
    box-shadow: 0 6px 18px rgba(0,0,0,0.12);
  }
  .letterhead .frame { position: absolute; inset: 0; }
  .letterhead .sheet-body {
    position: absolute; left: 46px; top: 46px; right: 46px; bottom: 46px;
    background: var(--paper);
    padding: 48px 54px 0 54px;
    color: var(--ink-blue);
  }
  .wordmark {
    display: flex; align-items: center; gap: 10px;
    color: var(--brand-blue);
    font-weight: 500;
    letter-spacing: 0.04em;
  }
  .wordmark .mark-square {
    width: 16px; height: 16px; background: var(--brand-blue);
  }
  .letterhead .wordmark { font-size: 20px; margin-left: 0; }
  .letter-title { font-size: 9.5px; font-weight: 700; margin-top: 68px; }
  .letter-copy { margin-top: 26px; font-size: 8.2px; line-height: 1.42; }
  .letter-copy p { margin-bottom: 11px; }
  .signature {
    margin-top: 30px; width: 62px; height: 30px;
    background: linear-gradient(90deg, rgba(10,74,120,0.12), rgba(10,74,120,0.04));
  }
  .signer { margin-top: 4px; font-size: 5.5px; letter-spacing: 0.22em; font-weight: 500; }
  .contact {
    position: absolute; left: 54px; bottom: 62px;
    font-size: 7.6px; letter-spacing: 0.12em; font-weight: 500; line-height: 1.3;
  }
  .contact .address { margin-bottom: 8px; }
  .contact .line { display: flex; align-items: center; gap: 6px; margin-bottom: 6px; }
  .contact svg { width: 9px; height: 9px; flex: none; }

  /* Envelope */
  .envelope {
    position: absolute; left: 630px; top: 560px;
    width: 530px; height: 300px;
  }
  .envelope .flap {
    position: absolute; left: 0; top: 0; width: 530px; height: 74px;
    border-radius: 14px 14px 0 0;
    background: var(--flap-blue);
  }
  .envelope .front {
    position: absolute; left: 0; top: 74px; width: 530px; height: 226px;
    background: var(--paper);
    box-shadow: 0 6px 18px rgba(0,0,0,0.12);
    display: flex; align-items: center; justify-content: center;
  }
  .envelope .wordmark { font-size: 22px; margin-left: 110px; }
</style>
</head>
<body>

<section class="letterhead" aria-label="Letterhead">
  <svg class="frame" width="565" height="800" viewBox="0 0 565 800">
    <g role="img" aria-label="Repeating monogram pattern border">
      <rect x="0" y="0" width="565" height="46" fill="var(--pattern-light)"/>
      <rect x="0" y="46" width="46" height="708" fill="var(--pattern-light)"/>
      <rect x="519" y="46" width="46" height="200" fill="var(--pattern-light)"/>
    </g>
    <g role="img" aria-label="Dark navy band with repeating monogram pattern">
      <polygon points="519,270 565,230 565,800 519,800" fill="var(--navy-band)"/>
      <polygon points="0,800 46,754 565,754 565,800" fill="var(--navy-band)"/>
    </g>
  </svg>

  <div class="sheet-body">
    <div class="wordmark"><span class="mark-square"></span>Moss Whitfield &amp; Danby LLP</div>

    <h1 class="letter-title">Branding</h1>
    <div class="letter-copy">
      <p>Branding is defined as the process of coming up or making a unique name or design for a certain product.</p>
      <p>Having a good brand strategy allows you to have a major advantage in gaining a large increase in your market competitions. Your brand tells your customers what they can expect from the products and services you offer.</p>
      <p>Are you innovative or are you the experienced type? Do you offer a high-cost, high-quality product, or a low-cost, high-value product? It's impossible to be both. You should consider thinking what your customers need you to be. Your logo is the main foundation of your brand. All the promotional materials should be connected with your logo to communicate with your brand.</p>
      <p>Brand messages are delivered and planned based on the questions how, what, when, to whom and where your brand strategy is. Advertisement, visual communication, and distribution channels are parts of brand strategy.</p>
      <p>The branding strategy you have should be consistent as it leads to a strong brand equity.</p>
    </div>
    <div class="signature" role="img" aria-label="Handwritten signature"></div>
    <div class="signer">NAME SURNAME</div>

    <div class="contact">
      <div class="address">LLP - 4827 LARKSPUR VALE ROAD,<br>IRVINE, CA<br>92614</div>
      <div class="line">
        <svg viewBox="0 0 10 10"><path d="M2 1 L4 1 L4.6 3 L3.5 4 Q4.5 6 6 6.5 L7 5.4 L9 6 L9 8 Q5 9 2.5 6 Q1 3.5 2 1Z" fill="currentColor"/></svg>
        (949)731-2864
      </div>
      <div class="line">
        <svg viewBox="0 0 10 10"><rect x="0.8" y="2" width="8.4" height="6" fill="none" stroke="currentColor" stroke-width="0.9"/><path d="M1 2.3 L5 5.5 L9 2.3" fill="none" stroke="currentColor" stroke-width="0.9"/></svg>
        CONTACT@MWDACCTS.EXAMPLE
      </div>
      <div class="line">
        <svg viewBox="0 0 10 10"><circle cx="5" cy="5" r="4" fill="none" stroke="currentColor" stroke-width="0.9"/><ellipse cx="5" cy="5" rx="1.8" ry="4" fill="none" stroke="currentColor" stroke-width="0.8"/><path d="M1 5 H9 M1.6 3 H8.4 M1.6 7 H8.4" stroke="currentColor" stroke-width="0.7"/></svg>
        WWW.MWDACCTS.EXAMPLE
      </div>
    </div>
  </div>
</section>

<section class="envelope" aria-label="Envelope">
  <div class="flap" role="img" aria-label="Envelope flap with repeating monogram pattern"></div>
  <div class="front">
    <div class="wordmark"><span class="mark-square"></span>Moss Whitfield &amp; Danby LLP</div>
  </div>
</section>

</body>
</html>
```